LABEL DESIGNS FOR SKINCARE LINE

Hello we are needing 12 label various label designs but would like to see you design ONE. We will pick winner from this and send the rest.
LABEL SIZE -2x7
JAR SIZE IS - 8oz
LOGOS FILES BELOW
https://vault.parcelnook.net/share/folders/7Kp3wQ-zrTbnvLoYcDFeMJHAXUw9PsR2a
INFORMATION FOR LABEL
Lumi Dawn Halo Whipped Body Sugar Scrub 8oz
Ideal for all Skin Types
Ingredients:
Pure Cane Sugar, Extra Virgin Coconut Oil, Mango Butter, Kukum Butter, Emulsifying Wax, Jojoba Seed Oil, Sweet Almond Oil, Strawberry Essential Oil, and Pomegranate Essential Oil.
Directions to use Body Sugar Scrub:
Apply to wet skin gently in a circular motion on desired body area, hands, feet, legs, arms, etc. Once you have a good scrub, rinse, pat dry, and enjoy soft, hydrated skin. Best to use in the shower. Use between 2-3 times a week if needed.
*Cautions:
(1) Allergy: Approach this product with extreme caution, if you have allergies
(2) Avoid direct contact with eyes
Storage/Shelf Life of Product:
For best results, stir/mix scrub with the wooden or plastic spoon before each use. The shelf life of all sugar scrubs is 6-8 weeks. Keep the product in a cool, dry place, away from hot or heated temperatures.
All Natural, Cruelty-Free, Vegan Free
No Mineral Oil
No Petroleum
No Parabens

```html
<!DOCTYPE html>
<html lang="en">
<head>
<meta charset="utf-8">
<title>Lumi Dawn Halo Whipped Body Sugar Scrub Label</title>
<link rel="stylesheet" href="https://fonts.googleapis.com/css2?family=Oswald:wght@600&family=Roboto+Condensed:wght@400;700&family=Open+Sans:wght@400&display=swap">
<style>
  :root {
    --page: #f2f1f0;
    --lilac-light: #ddcfe0;
    --lilac: #cbb7cf;
    --magenta: #b3157f;
    --ink: #2b2230;
    --gold: #c9a03a;
    --gold-dark: #a67d22;
    --box: #f4f0f5;
  }
  * { margin: 0; padding: 0; box-sizing: border-box; }
  html, body { width: 1200px; height: 1200px; overflow: hidden; background: var(--page); }
  body { display: flex; align-items: center; justify-content: center; }

  .label {
    position: relative;
    width: 1200px;
    height: 343px;
    background: linear-gradient(180deg, var(--lilac-light) 0%, var(--lilac) 100%);
    border-top: 3px solid var(--gold);
    border-bottom: 3px solid var(--gold);
    display: grid;
    grid-template-columns: 330px 1fr 330px;
    font-family: "Roboto Condensed", sans-serif;
    color: var(--ink);
  }
  .label::before, .label::after {
    content: ""; position: absolute; left: 0; right: 0; height: 1px; background: var(--gold-dark);
  }
  .label::before { top: 4px; }
  .label::after { bottom: 4px; }

  .panel { padding: 26px 24px; font-size: 12.5px; line-height: 1.38; }
  .panel h3 { font-size: 13px; font-weight: 700; text-transform: uppercase; margin-bottom: 2px; }
  .panel p { margin-bottom: 14px; text-align: justify; }

  .storage-title { text-transform: none; }
  .claims { font-weight: 700; font-size: 12px; margin-bottom: 8px; }
  .badges { display: flex; gap: 10px; margin-bottom: 14px; }
  .badge { width: 36px; height: 36px; border-radius: 50%; background: radial-gradient(circle at 35% 30%, #e6c46a, var(--gold) 60%, var(--gold-dark)); }
  .detail-box { background: var(--box); border-radius: 4px; padding: 8px 10px; font-weight: 700; font-size: 12px; margin-bottom: 8px; }
  .maker { font-size: 11px; line-height: 1.35; }

  .front { display: flex; flex-direction: column; align-items: center; padding-top: 60px; position: relative; }
  .brand { font-family: "Roboto Condensed", sans-serif; font-weight: 700; font-size: 62px; color: var(--magenta); letter-spacing: 0.5px; line-height: 1; display: flex; align-items: center; gap: 12px; }
  .brand-dot { width: 12px; height: 12px; border-radius: 50%; background: var(--magenta); }
  .product-band { margin-top: 48px; background: var(--magenta); color: #fff; font-family: "Oswald", sans-serif; font-weight: 600; font-size: 30px; padding: 2px 12px; letter-spacing: 0.5px; line-height: 1.25; text-transform: uppercase; }
  .product-type { align-self: flex-start; margin-left: 86px; font-family: "Oswald", sans-serif; font-weight: 600; font-size: 23px; color: var(--magenta); letter-spacing: 0.8px; text-transform: uppercase; line-height: 1.2; margin-top: 4px; }
  .skin { align-self: flex-start; margin-left: 86px; font-family: "Open Sans", sans-serif; font-size: 18px; letter-spacing: 0.6px; }
  .net { position: absolute; bottom: 18px; font-weight: 700; font-size: 15px; }
</style>
</head>
<body>
  <main class="label">
    <section class="panel panel-left">
      <h3 class="storage-title">Storage/Shelf Life of Product:</h3>
      <p>For best results, stir/mix scrub with the wooden or plastic spoon before each use. The shelf life of all sugar scrubs is 6-8 weeks. Keep the product in a cool, dry place, away from hot or heated temperatures.</p>
      <div class="claims">All Natural, Cruelty-Free, Vegan Free</div>
      <div class="badges">
        <span class="badge" aria-hidden="true"></span>
        <span class="badge" aria-hidden="true"></span>
        <span class="badge" aria-hidden="true"></span>
      </div>
      <div class="detail-box">Add other detail here<br>&lt;mfg. date&gt; &lt;exp. date&gt; &lt;mrp&gt; etc.</div>
      <div class="maker">Made &amp; Distributed by &lt;Name&gt;&lt;City&gt;&lt;Country&gt;<br>Visit us: &lt;www.website.com&gt;<br>Help &amp; email: support@yourid.com</div>
    </section>

    <section class="front">
      <div class="brand"><span>Petal Hush &amp; Co</span><span class="brand-dot" aria-hidden="true"></span></div>
      <div class="product-band">Lumi Dawn Halo Whipped</div>
      <div class="product-type">Body Sugar Scrub</div>
      <div class="skin">Ideal for all Skin Types</div>
      <div class="net">Net WT 8 fl oz</div>
    </section>

    <section class="panel panel-right">
      <h3>Ingredients:</h3>
      <p>Pure Cane Sugar, Extra Virgin Coconut Oil, Mango Butter, Kukum Butter, Emulsifying Wax, Jojoba Seed Oil, Sweet Almond Oil, Strawberry Essential Oil, and Pomegranate Essential Oil.</p>
      <h3>Directions to use Body Sugar Scrub:</h3>
      <p>Apply to wet skin gently in a circular motion on desired body area, hands, feet, legs, arms, etc. Once you have a good scrub, rinse, pat dry, and enjoy soft, hydrated skin. Best to use in the shower. Use between 2-3 times a week if needed.</p>
      <h3>Cautions:</h3>
      <p>1) Allergy: Approach this product with extreme caution, if you have allergies. 2) Avoid direct contact with eyes.</p>
    </section>
  </main>
</body>
</html>
```